Veterinary TPLO Surgery Flyer Design

Please use this flyer to make a professional-looking 1 page, double-sided client handout regarding TPLO.

You can visit our website at www.brookferrypetcare.com & www.northgroveanimalsurgery.com for additional logo information. The flyer should include all the text from the one provided.

Target Market(s)

Client communication to for referral surgery between sister veterinary clinics

Industry/Entity Type

Veterinary

Requirements
Must have
• The text included
Nice to have
• Nice to have the Willow Crest Avenue Animal CLinic & Dr. Pettigrew Mobile vet logos incorporated.

```html
<!DOCTYPE html>
<html lang="en">
<head>
<meta charset="utf-8">
<title>TPLO Surgery Client Handout</title>
<link rel="stylesheet" href="https://fonts.googleapis.com/css2?family=Bebas+Neue&family=Roboto:ital,wght@0,400;0,700;1,400&display=swap">
<style>
:root{
  --backdrop:#3a3a3a;
  --paper:#ffffff;
  --rust:#843a1e;
  --rust-deep:#6e2f17;
  --clay:#b8623a;
  --orange:#e5804f;
  --heading:#b4592c;
  --ink:#2e2e2e;
}
*{margin:0;padding:0;box-sizing:border-box}
html,body{width:1200px;height:845px;overflow:hidden;background:var(--backdrop)}
body{position:relative;font-family:"Roboto",Arial,sans-serif;color:var(--ink)}
.page{position:absolute;top:67px;width:507px;height:717px;background:var(--paper);overflow:hidden}
.page-front{left:79px}
.page-back{left:614px}
.abs{position:absolute}

/* front */
.clinic-band{left:0;top:0;width:213px;height:56px;background:var(--clay)}
.clinic-name{left:22px;top:11px;color:#fff;font-size:14px;line-height:17px;font-weight:400}
.title-band{left:203px;top:14px;width:304px;height:112px;background:var(--rust)}
.title{left:235px;top:22px;color:#fff;font-family:"Bebas Neue",Impact,sans-serif;font-size:42px;line-height:39px;letter-spacing:.5px}
.byline{left:235px;top:104px;color:#fff;font-size:11.5px;font-weight:700}
.portrait{left:0;top:56px;width:208px;height:220px;background:radial-gradient(ellipse at 45% 45%,#e2b08e 0%,#efd6c4 40%,#fbf4ee 75%,#fff 100%)}
.tagline{left:235px;top:133px;font-size:10px;font-style:italic}
.about-heading{left:235px;top:162px;font-size:20px;font-weight:700;color:var(--rust)}
.about-text{left:235px;top:193px;width:262px;font-size:9.6px;line-height:14px}
.about-more{left:20px;top:281px;width:470px;font-size:9.6px;line-height:12px}
.card{border:1.2px solid var(--orange);border-radius:14px}
.card-what{left:15px;top:313px;width:235px;height:175px}
.card-benefits{left:17px;top:500px;width:237px;height:176px}
.h-orange{font-size:15px;font-weight:700;color:var(--heading);line-height:18px}
.card-what .h-orange{position:absolute;left:10px;top:10px}
.card-what p{position:absolute;left:10px;top:39px;width:215px;font-size:9.6px;line-height:15.8px}
.card-benefits .h-orange{position:absolute;left:10px;top:12px}
.benefit-list{position:absolute;left:10px;top:46px;width:220px;list-style:none;font-size:9.6px;line-height:12.2px}
.benefit-list li{margin-bottom:11px}
.why-heading{left:270px;top:322px;width:230px}
.why-text{left:270px;top:372px;width:222px;font-size:9.6px;line-height:14px}
.band-low{left:0;top:689px;width:251px;height:28px;background:var(--orange)}
.band-fold{left:251px;top:676px;width:19px;height:41px;background:var(--rust)}
.band-high{left:270px;top:676px;width:237px;height:41px;background:var(--orange)}

/* back */
.cat-photo{left:0;top:0;width:507px;height:300px;background:linear-gradient(120deg,#8a6a4c 0%,#c9b19a 35%,#f2ebe4 60%,#e7d8cc 80%,#b49c86 100%)}
.top-band{left:0;top:0;width:245px;height:35px}
.badge{left:31px;top:0;width:96px;height:108px}
.badge-name{left:31px;top:50px;width:96px;text-align:center;font-size:9px;line-height:11px;font-weight:700;color:var(--rust)}
.rust-flag{left:296px;top:243px;width:211px;height:37px}
.thumb{top:195px;width:122px;height:107px;border-radius:10px}
.thumb-model{left:18px;background:linear-gradient(180deg,#d8d4dc,#ece6dc)}
.thumb-xray{left:161px;background:linear-gradient(90deg,#111,#3a3a3a 40%,#1a1a1a 70%,#555)}
.frame{left:11px;top:291px;width:486px;height:470px;border:1.5px solid var(--orange);border-radius:16px}
.process-heading{left:25px;top:316px}
.process-list{left:25px;top:347px;width:230px;font-size:9.4px;line-height:12.3px;list-style:none}
.process-list li{margin-bottom:0}
.process-list li:first-child{margin-bottom:8px}
.info-head{background:var(--orange);color:#fff;font-weight:700}
.post-head{left:267px;top:311px;width:240px;height:45px;padding:5px 0 0 14px;font-size:9.6px;line-height:12.2px}
.post-text{left:273px;top:367px;width:226px;font-size:9.4px;line-height:12.2px}
.post-text p{margin-bottom:8px}
.contact-head{left:263px;top:507px;width:244px;height:28px;padding:4px 0 0 16px;font-size:10px;font-weight:400;line-height:11px}
.contact-head small{font-size:7.5px;font-weight:700;display:block}
.mobile-head{left:263px;top:606px;width:244px;height:31px;padding:3px 0 0 16px;font-size:10px;line-height:13px}
.contact-row{display:flex;align-items:center;gap:6px;font-size:10px;height:15.5px}
.contact-row svg{width:10px;height:10px;flex:none}
.clinic-contacts{left:273px;top:538px}
.mobile-contacts{left:282px;top:646px}
.back-band-low{left:0;top:681px;width:238px;height:36px;background:var(--orange)}
.back-band-fold{left:238px;top:681px;width:18px;height:36px;background:var(--rust)}
.back-band-high{left:256px;top:694px;width:251px;height:23px;background:var(--orange)}
</style>
</head>
<body>

<section class="page page-front">
  <div class="abs clinic-band"></div>
  <div class="abs clinic-name">Willow Crest Avenue<br>Animal Clinic</div>
  <svg class="abs" style="left:203px;top:56px" width="12" height="14"><polygon points="0,0 12,0 0,14" fill="#b8623a"/></svg>
  <div class="abs title-band"></div>
  <h1 class="abs title">Advanced<br>Orthopedic Care</h1>
  <div class="abs byline">by Dr. Helena Pettigrew, DVM, DACVS-sa</div>
  <div class="abs portrait" role="img" aria-label="Watercolor illustration of a veterinarian hugging an orange cat"></div>

  <p class="abs tagline">TPLO Surgery at Willow Crest Avenue Animal Clinic About</p>
  <h2 class="abs about-heading">Dr. Helena Pettigrew is</h2>
  <p class="abs about-text">a board-certified veterinary surgeon (Diplomate of the National College of Veterinary Surgeons) with over 18 years of experience in small animal surgery. A graduate of Great Lakes State University, she completed her surgical residency at Harborview School of Veterinary Medicine. Through her mobile</p>
  <p class="abs about-more">practice, Northgrove Mobile Surgery, Dr. Pettigrew now provides advanced surgical procedures—such as TPLO directly at local clinics.</p>

  <div class="abs card card-what">
    <h3 class="h-orange">What is TPLO Surgery?</h3>
    <p>Tibial Plateau Leveling Osteotomy (TPLO) is a surgical procedure that stabilizes the stifle (knee) joint following a cranial cruciate ligament (CCL) rupture—a common orthopedic injury in dogs. The procedure involves altering the angle of the tibial plateau to eliminate abnormal joint motion, restoring stability and improving function.</p>
  </div>

  <div class="abs card card-benefits">
    <h3 class="h-orange">Benefits of TPLO Surgery</h3>
    <ul class="benefit-list">
      <li>● Enhanced Joint Stability: Restores natural biomechanics, reducing pain and improving mobility.</li>
      <li>● Faster Recovery: Many dogs return to normal activity faster compared to other surgical techniques.</li>
      <li>● Proven Long-Term Success: TPLO is particularly effective in large and active breeds.</li>
    </ul>
  </div>

  <h3 class="abs h-orange why-heading">Why Choose Willow Crest Avenue Animal Clinic?</h3>
  <p class="abs why-text">Partnering with Dr. Pettigrew, Willow Crest Avenue Animal Clinic offers advanced orthopedic surgery<br>on-site—eliminating the need for referrals or travel. This collaboration ensures your pet receives expertsurgical care in a familiar, trusted environment. Our clinic works directly with your primary veterinarian to share medical records, diagnostics, and prescriptions, ensuring seamless and coordinated care for your pet. Diagnostic Radiographs vs. TPLO Planning Radiographs While diagnostic radiographs may confirm a CCL tear, they are not sufficient for surgical planning.TPLO requires three advanced technique radiographic views with precise measurements, which must be performed under sedation to reduce discomfort and allow accurate positioning.stability and improving function.</p>

  <div class="abs band-low"></div>
  <div class="abs band-fold"></div>
  <div class="abs band-high"></div>
</section>

<section class="page page-back">
  <div class="abs cat-photo" role="img" aria-label="Photo of a calico cat lying on gravel, paw raised"></div>
  <svg class="abs top-band" viewBox="0 0 245 35"><polygon points="0,0 245,0 237,35 0,35" fill="#b8623a"/></svg>
  <svg class="abs badge" viewBox="0 0 96 108"><path d="M0,0 H96 V70 Q96,108 48,108 Q0,108 0,70 Z" fill="#fff"/></svg>
  <div class="abs badge-name">Dr. Pettigrew<br>Mobile Vet</div>
  <svg class="abs rust-flag" viewBox="0 0 211 37"><polygon points="0,0 211,0 211,37 6,37" fill="#843a1e"/></svg>
  <div class="abs thumb thumb-model" role="img" aria-label="Technical drawing of the stifle joint before and after TPLO"></div>
  <div class="abs thumb thumb-xray" role="img" aria-label="Pre-op and post-op TPLO radiographs"></div>

  <div class="abs frame"></div>

  <h3 class="abs h-orange process-heading">Expected Process</h3>
  <ol class="abs process-list">
    <li>1. Diagnosis: Your pet is diagnosed with stifle</li>
    <li>instability (CCL tear) by your veterinarian.</li>
    <li>2. Referral: Your veterinarian contacts the surgical coordinator at Willow Crest Avenue Animal Clinic.</li>
    <li>3. Consultation: The coordinator contacts you to schedule a 1-hour consultation to review the procedure, estimated costs, and available surgery dates.</li>
    <li>4. Planning Radiographs: These specialized X-rays are typically taken during the consultation under light sedation.</li>
    <li>5. Surgical Review: Dr. Pettigrew reviews the radiographs and your pet’s medical history to confirm<br>candidacy for TPLO.</li>
    <li>6. Deposit: A $3,500 deposit secures Dr. Pettigrew’s travel and surgery date. This is refundable if canceled at least 5 days prior to the scheduled procedure.</li>
    <li>7. Surgery Day: Your pet is dropped off in the morning and surgery is performed the same day.</li>
    <li>8. Discharge: You’ll receive a post-surgery update and your pet will go home that evening</li>
  </ol>

  <div class="abs info-head post-head">Post-Operative Care &amp; Follow-Up<br>Two follow-up appointments will be<br>scheduled:</div>
  <div class="abs post-text">
    <p>● <b>4 Weeks Post-Op</b>: Evaluate healing, refill medications, and address any questions.</p>
    <p>● <b>8 Weeks Post-Op</b>: Sedated radiographs will confirm proper healing of the surgical site and tibia.</p>
    <p><b>Dr. Pettigrew</b> will stay in direct contact with you during your pet’s recovery using her custom <b>mobile app,</b><br>which allows for secure messaging and provides detailed post-operative instructions</p>
  </div>

  <div class="abs info-head contact-head"><small>Contact Information:</small>Willow Crest Avenue Animal Clinic</div>
  <div class="abs clinic-contacts">
    <div class="contact-row"><svg viewBox="0 0 10 10"><path d="M5 9.5C2.5 6.5 1.5 5 1.5 3.5a3.5 3.5 0 0 1 7 0C8.5 5 7.5 6.5 5 9.5Z" fill="none" stroke="#e5804f" stroke-width=".9"/></svg>2280 Willow Crest Avenue, Brookferry, MI 48930</div>
    <div class="contact-row"><svg viewBox="0 0 10 10"><path d="M2 1l2 2-1 1.3a6 6 0 0 0 2.7 2.7L7 6l2 2-1.3 1.3C4.5 9 1 5.5.7 2.3Z" fill="none" stroke="#e5804f" stroke-width=".9"/></svg>(517) 555-0142</div>
    <div class="contact-row"><svg viewBox="0 0 10 10"><rect x=".5" y="2" width="9" height="6.5" fill="none" stroke="#e5804f" stroke-width=".9"/><path d="M.5 2L5 6l4.5-4" fill="none" stroke="#e5804f" stroke-width=".9"/></svg>info@brookferrypetcare.com</div>
    <div class="contact-row"><svg viewBox="0 0 10 10"><circle cx="5" cy="5" r="4.4" fill="none" stroke="#e5804f" stroke-width=".9"/><ellipse cx="5" cy="5" rx="2" ry="4.4" fill="none" stroke="#e5804f" stroke-width=".8"/><path d="M.6 5h8.8M1.3 3h7.4M1.3 7h7.4" stroke="#e5804f" stroke-width=".7"/></svg>www.brookferrypetcare.com</div>
  </div>

  <div class="abs info-head mobile-head">Northgrove Mobile Surgery<br>(Dr. Helena Pettigrew)</div>
  <div class="abs mobile-contacts">
    <div class="contact-row"><svg viewBox="0 0 10 10"><path d="M2 1l2 2-1 1.3a6 6 0 0 0 2.7 2.7L7 6l2 2-1.3 1.3C4.5 9 1 5.5.7 2.3Z" fill="none" stroke="#e5804f" stroke-width=".9"/></svg>&nbsp;&nbsp;(810) 555-0187</div>
    <div class="contact-row"><svg viewBox="0 0 10 10"><rect x=".5" y="2" width="9" height="6.5" fill="none" stroke="#e5804f" stroke-width=".9"/><path d="M.5 2L5 6l4.5-4" fill="none" stroke="#e5804f" stroke-width=".9"/></svg>&nbsp;&nbsp;drpettigrew@northgrovemobilesurgery.com</div>
    <div class="contact-row"><svg viewBox="0 0 10 10"><circle cx="5" cy="5" r="4.4" fill="none" stroke="#e5804f" stroke-width=".9"/><ellipse cx="5" cy="5" rx="2" ry="4.4" fill="none" stroke="#e5804f" stroke-width=".8"/><path d="M.6 5h8.8M1.3 3h7.4M1.3 7h7.4" stroke="#e5804f" stroke-width=".7"/></svg>&nbsp;&nbsp;www.northgroveanimalsurgery.com</div>
  </div>

  <div class="abs back-band-low"></div>
  <div class="abs back-band-fold"></div>
  <div class="abs back-band-high"></div>
</section>

</body>
</html>
```